Author needs a new book, Kindle and Audiobook cover design

I updated and re-edited a book I wrote 25 years ago but now realize the title and design did not get the job done. I am seeking a book, Kindle and audiobook design that will make me stand out. The final design will pop while being sensitive to the nature of the subject. The title of the book is Quiet Lanterns. Subtitle: Ways to Notice and Step Away From Harmful Circles While Keeping Steady Belief by Dorian T. Wexcombe. I am wanting to get the attention of people who have been damaged by a church relationship that started well but ended badly.
Updates

The book title is: Quiet Lanterns. The Subtitle is: Ways To Notice and Step Away From Harmful Circles While Keeping Steady Belief. The dimension is 6x9 (150 pages) and I am the author: Dorian T. Wexcombe

Target Market(s)

People with a church experience; church leadership. Religious abuse victims.

Industry/Entity Type

Christian

Font styles to use
Serif

Colors

Designer to choose colors to be used in the design.

Requirements
Nice to have
• I am not married to the Serif font if another design works better.

```html
<!DOCTYPE html>
<html lang="en">
<head>
<meta charset="utf-8">
<title>Quiet Lanterns — Dorian T. Wexcombe</title>
<link rel="stylesheet" href="https://fonts.googleapis.com/css2?family=Cinzel:wght@400;500&family=Montserrat:wght@400&display=swap">
<style>
  :root {
    --bg-deep: #050404;
    --glow-core: #6a5b4c;
    --glow-mid: #2e2620;
    --title-beige: #d9c3a6;
    --subtitle-white: #f2eee8;
    --author-beige: #d6c2a8;
    --cross-wood: #7a3f22;
    --cross-wood-dark: #4a2412;
  }
  * { margin: 0; padding: 0; box-sizing: border-box; }
  html, body {
    width: 800px;
    height: 1200px;
    overflow: hidden;
    background: var(--bg-deep);
  }
  .book-cover {
    position: relative;
    width: 800px;
    height: 1200px;
    overflow: hidden;
    background:
      radial-gradient(ellipse 62% 48% at 50% 62%, var(--glow-core) 0%, var(--glow-mid) 45%, var(--bg-deep) 100%);
  }
  .cover-title {
    position: absolute;
    top: 18px;
    left: 0;
    width: 100%;
    text-align: center;
    font-family: "Cinzel", serif;
    font-weight: 500;
    color: var(--title-beige);
    font-size: 118px;
    line-height: 132px;
    letter-spacing: 2px;
    text-transform: uppercase;
  }
  .cover-title span { display: block; }
  .cover-subtitle {
    position: absolute;
    top: 388px;
    left: 70px;
    width: 660px;
    text-align: center;
    font-family: "Montserrat", sans-serif;
    font-weight: 400;
    color: var(--subtitle-white);
    font-size: 19px;
    line-height: 33px;
    letter-spacing: 0.5px;
    text-transform: uppercase;
  }
  .cover-emblem {
    position: absolute;
    left: 355px;
    top: 800px;
    width: 108px;
    height: 156px;
  }
  .cover-author {
    position: absolute;
    top: 1068px;
    left: 0;
    width: 100%;
    text-align: center;
    font-family: "Cinzel", serif;
    font-weight: 400;
    color: var(--author-beige);
    font-size: 34px;
    letter-spacing: 4px;
    text-transform: uppercase;
  }
</style>
</head>
<body>
  <main class="book-cover">
    <h1 class="cover-title"><span>Quiet</span><span>Lanterns</span></h1>
    <p class="cover-subtitle">Ways To Notice and Step Away From Harmful Circles<br>While Keeping Steady Belief</p>
    <svg class="cover-emblem" viewBox="0 0 108 156" role="img" aria-label="Small rustic wooden cross illustration">
      <defs>
        <linearGradient id="woodTone" x1="0" y1="0" x2="1" y2="1">
          <stop offset="0" stop-color="var(--cross-wood)"/>
          <stop offset="1" stop-color="var(--cross-wood-dark)"/>
        </linearGradient>
      </defs>
      <rect x="45" y="0" width="18" height="156" fill="url(#woodTone)"/>
      <rect x="0" y="34" width="108" height="17" fill="url(#woodTone)"/>
    </svg>
    <p class="cover-author">Dorian T. Wexcombe</p>
  </main>
</body>
</html>
```